Cafe / Bistro Website with a focus on Salads

I will be creating a wordpress site from the psds that you provide to me, i have attached a questionnaire and the answers to them to get an idea of what I'm looking for.

Reason: Id like to provide more time for designers to submit your designs, good luck!

Target Market(s)

20 - 45 years old downtown professionals

Industry/Entity Type

Cafe

Number of Pages Required

1 page

Requirements
Must have
• 1. Describe the products/services you sell.
• Cafe is open for breakfast and lunch serving fresh, made from scratch
• food and bakery items with an emphasis on their Fresh Bakery, Coffee,
• Panini & Deli Sandwiches, Fresh Salads with Homemade Dressings,
• Retail Items and Breakfast Items. (salads and dressings are their hottest
• selling items)
• 2. Age range of your target client base
• 20 - 45 years old
• Project-related questions
• 3. Technical skill level of your client base. Have a scale ranging from zero to ten with zero
• being the least technologically skilled and ten being the best.
• From 8 to 9 scale for tech savvy customers so mobile friendly is a must
• have.
Nice to have
• 4. Will your visitors require any special needs? Mobile version of site, multiple language
• support, larger type for easier reading, etc.)
• Just need the mobile friendly version as well.
• 5. Imagine your website in 5 years from now. Complete the sentence: I know my website works
• because…
• I know my website works because we have seen an increase in steady
• business and we are seeing new customers because of our online
• presence.
• 6. Name 3 things that are most important about the design of your new website.
• Branding matches our store look and feel, website has a clean look and
• its easy to read/user friendly.
• 7. Name 3 things that is least important in the design of your new website.
• 12. We don't need very much content, just enough to get them interested
• in visiting our store.
• 8. Do you have any color preferences, existing brand colors, and/or colors you do/not wish to
• include?
• Yes, we have uploaded a few interior pics not to be used on the site, but
• mainly for color and wood texture examples. Do your best to match the
• wood grain textures and the colors. A fun coffee cup similar to ours
• would be cool if its easy to create in Illustrator or Photoshop.
• 9. What are some existing websites that appeal to you? Provide links if possible.
• Not sure what sites I like that fit our store look and feel, sorry ;(
• © All Rights Reserved by lumen Brightpath IT 3
• Additional questions
• 10. Is your logo and other imagery web ready?
• 11. Do you have all images that you would like to be included in your website or would you like
• the designer to use imagery where appropriate?
• We can use stock photography where they see appropriate. I would like
• to use my food photos and merchandise photos, but maybe those are not
• seen on the home page? We can adjust once we see the first draft of the
• website designs.
• 12. Any specific features you would like included? Log in ability, calendars, forums, blog,
• subscription services (RSS, email or newsletters)?
• The only feature I could see using would be a calendar with days listing
• my type of soups and daily specials available. I should be able to know
• what those items are the last week of the month for the upcoming month.
• That would be cool and force me to be more organized with thinking
• ahead of time.
• PICKS RELATED AND MENTIONED ABOVE CAN ALL BE
• FOUND HERE…
• https://www.filevaultra.com/sh/qtrbwmkeyzlpaxv/BBkTpQ4mNcWuZyrfdhSJqoPa?dl=0

```html
<!DOCTYPE html>
<html lang="en">
<head>
<meta charset="utf-8">
<title>Milo's Cafe</title>
<link href="https://fonts.googleapis.com/css2?family=Lora:wght@400;700&family=Open+Sans:wght@400;600;700&family=Oswald:wght@500;700&display=swap" rel="stylesheet">
<style>
:root{
  --red:#8c1b1f;
  --red-dark:#5a1216;
  --ink:#1b1b1b;
  --nav:#161616;
  --paper:#f3f1ee;
  --text:#555;
  --muted:#8a8580;
  --wood:#5b3a24;
  --chalk:#222;
  --white:#fff;
}
*{margin:0;padding:0;box-sizing:border-box}
html,body{width:853px;height:1200px;overflow:hidden}
body{font-family:"Open Sans",Arial,sans-serif;background:var(--white);color:var(--text);position:relative}

.topbar{height:93px;background:var(--paper);position:relative}
.social{position:absolute;left:34px;top:34px;display:flex;gap:8px}
.social span{width:24px;height:24px;border-radius:50%;border:1px solid #bbb;background:var(--white)}
.call{position:absolute;right:34px;top:30px;display:flex;align-items:center;gap:10px;text-align:right}
.call small{display:block;font-size:10px;color:var(--muted)}
.call strong{font-size:17px;color:var(--red);font-weight:700}
.call .icon{width:32px;height:32px;border-radius:50%;background:var(--red);display:flex;align-items:center;justify-content:center}

.brand{position:absolute;left:366px;top:6px;width:120px;height:120px;border-radius:50%;background:var(--red-dark);border:4px solid var(--paper);display:flex;align-items:center;justify-content:center;z-index:3}
.brand span{font-family:"Lora",Georgia,serif;font-weight:700;color:var(--white);font-size:19px}

.nav{height:29px;background:var(--nav);position:relative}
.nav-group{position:absolute;top:0;display:flex}
.nav-group.left{left:28px}
.nav-group.right{left:505px}
.nav a{font-size:10px;font-weight:600;color:#ddd;text-decoration:none;letter-spacing:.5px;padding:0 14px;line-height:29px}
.nav a.active{background:var(--red);color:var(--white)}

.hero{height:361px;position:relative;background:radial-gradient(ellipse at 70% 55%,#8a5a33 0%,#4a2d1a 45%,#1e140e 100%)}
.hero-copy{position:absolute;left:210px;top:110px;color:var(--white)}
.hero-copy .hi{font-family:"Oswald",sans-serif;font-size:22px;font-weight:500;letter-spacing:1px}
.hero-copy .name{font-family:"Oswald",sans-serif;font-size:72px;font-weight:700;line-height:.95}
.hero-copy .tag{font-family:"Oswald",sans-serif;font-size:17px;letter-spacing:1px;border-top:2px solid var(--white);padding-top:4px;margin-top:4px}

.welcome{height:322px;display:flex;padding:32px 34px 0 34px;gap:36px}
.welcome .copy{width:470px}
.welcome h1{font-family:"Lora",Georgia,serif;font-size:24px;color:var(--ink);font-weight:700;margin-bottom:12px}
.welcome p{font-size:10.5px;line-height:1.7;margin-bottom:14px}
.btn{display:inline-block;background:var(--red);color:var(--white);font-size:10px;padding:6px 12px;text-decoration:none}

.special{width:280px}
.special .board{background:var(--chalk);border:6px solid var(--wood);padding:14px 18px;color:#eee}
.special h2{font-family:"Lora",Georgia,serif;font-size:24px;font-weight:400;border-bottom:1px solid #666;padding-bottom:8px;margin-bottom:8px}
.special table{width:100%;border-collapse:collapse;font-size:10px}
.special td{padding:7px 0;border-bottom:1px dashed #555}
.special td:last-child{text-align:right}
.special .btn{display:block;text-align:center;margin-top:6px}

.menu{height:185px;background:linear-gradient(#332c27,#241f1b);position:relative;text-align:center;padding-top:12px}
.menu h2{font-family:"Lora",Georgia,serif;font-size:24px;font-weight:400;color:var(--white);margin-bottom:12px}
.cards{display:flex;justify-content:center;gap:18px}
.card{width:150px}
.card .photo{height:100px;border:3px solid var(--white)}
.card p{font-size:11px;color:var(--white);font-weight:600;margin-top:6px}
.arrow{position:absolute;top:96px;width:18px;height:30px}
.arrow.left{left:56px}.arrow.right{right:56px}

.footer{height:182px;background:var(--red-dark);display:flex;padding:22px 34px 0}
.footer .logo{width:270px;display:flex;align-items:flex-start;padding-left:40px}
.footer .logo div{width:110px;height:110px;border-radius:50%;border:2px solid #8f3a3e;display:flex;align-items:center;justify-content:center}
.footer .logo span{font-family:"Lora",Georgia,serif;font-weight:700;color:#e9d9d9;font-size:17px}
.footer h3{font-family:"Lora",Georgia,serif;font-size:14px;font-weight:400;color:var(--white);margin-bottom:8px}
.footer ul{list-style:none;font-size:9.5px;color:#e6cfcf;line-height:1.75}
.col-links{width:150px}
.col-contact{width:200px}
.col-contact p{font-size:9.5px;color:#e6cfcf;line-height:1.6;margin-bottom:6px}
.follow li{display:flex;align-items:center;gap:8px;margin-bottom:5px}
.follow i{width:16px;height:16px;border-radius:50%;background:#e6cfcf;display:inline-block}

.legal{height:28px;background:#2a0b0d;display:flex;justify-content:space-between;align-items:center;padding:0 34px;font-size:9px;color:#bfa6a6}
</style>
</head>
<body>
<header class="topbar">
  <div class="social"><span></span><span></span><span></span></div>
  <div class="brand"><span>Milo's Cafe</span></div>
  <div class="call">
    <div><small>Call Us</small><strong>01-5550-4821</strong></div>
    <div class="icon"><svg width="14" height="14" viewBox="0 0 24 24"><path fill="#fff" d="M6.6 10.8a15 15 0 0 0 6.6 6.6l2.2-2.2c.3-.3.7-.4 1-.2 1.1.4 2.3.6 3.6.6.6 0 1 .4 1 1V20c0 .6-.4 1-1 1A17 17 0 0 1 3 4c0-.6.4-1 1-1h3.5c.6 0 1 .4 1 1 0 1.3.2 2.5.6 3.6.1.3 0 .7-.2 1z"/></svg></div>
  </div>
</header>
<nav class="nav">
  <div class="nav-group left"><a class="active" href="#">HOME</a><a href="#">ABOUT US</a><a href="#">COFFEE</a></div>
  <div class="nav-group right"><a href="#">MENU</a><a href="#">CALENDAR</a><a href="#">CONTACT US</a></div>
</nav>

<section class="hero" role="img" aria-label="Chef plating a dish beside a red coffee cup in a warm cafe kitchen">
  <div class="hero-copy">
    <div class="hi">HI I'M</div>
    <div class="name">MILO &amp;</div>
    <div class="tag">I MAKE GREAT FOOD &amp; COFFEE</div>
  </div>
</section>

<section class="welcome">
  <div class="copy">
    <h1>Welcome to Milo's Cafe</h1>
    <p>Lorem ipsum dolor sit amet, consectetuer adipiscing elit, sed diam nonummy nibh euismod tincidunt ut laoreet dolore magna aliquam erat volutpat. Ut wisi enim ad minim veniam, quis nostrud exerci tation ullamcorper suscipit lobortis nisl ut aliquip ex ea commodo consequat. Duis autem vel eum iriure dolor in hendrerit in vulputate velit esse molestie consequat, vel illum dolore eu feugiat nulla facilisis at vero eros et accumsan et iusto odio dignissim qui blandit praesent luptatum zzril delenit augue duis dolore te feugait.</p>
    <p>Lorem ipsum dolor sit amet, consectetuer adipiscing elit, sed diam nonummy nibh euismod tincidunt.</p>
    <a class="btn" href="#">Read More</a>
  </div>
  <aside class="special">
    <div class="board">
      <h2>Today Special</h2>
      <table>
        <tr><td>Lorem ipsum dolor</td><td>8am to 10am</td></tr>
        <tr><td>Ullamcorper suscipit</td><td>9am to 10am</td></tr>
        <tr><td>Desserts and Cakes</td><td>11am to 3.30pm</td></tr>
        <tr><td>Coffee</td><td>8am to 6pm</td></tr>
      </table>
    </div>
    <a class="btn" href="#">View Menu Calendar</a>
  </aside>
</section>

<section class="menu">
  <h2>Our Menu</h2>
  <svg class="arrow left" viewBox="0 0 18 30"><path d="M15 3 3 15l12 12" fill="none" stroke="#fff" stroke-width="3"/></svg>
  <div class="cards">
    <div class="card"><div class="photo" role="img" aria-label="Cup of coffee" style="background:linear-gradient(135deg,#6b4630,#2b1a10)"></div><p>Coffee</p></div>
    <div class="card"><div class="photo" role="img" aria-label="Panini sandwich" style="background:linear-gradient(135deg,#c99a5b,#7a5030)"></div><p>Panini &amp; Deli Sandwiches</p></div>
    <div class="card"><div class="photo" role="img" aria-label="Fresh salad bowl" style="background:linear-gradient(135deg,#9cc266,#c84a3a)"></div><p>Fresh Salads</p></div>
    <div class="card"><div class="photo" role="img" aria-label="Breakfast plate" style="background:linear-gradient(135deg,#e8c07a,#a35a2e)"></div><p>Breakfast Items</p></div>
  </div>
  <svg class="arrow right" viewBox="0 0 18 30"><path d="M3 3l12 12L3 27" fill="none" stroke="#fff" stroke-width="3"/></svg>
</section>

<footer class="footer">
  <div class="logo"><div><span>Milo's Cafe</span></div></div>
  <div class="col-links">
    <h3>Quick Link</h3>
    <ul><li>Home</li><li>About Us</li><li>Coffee</li><li>Menu</li><li>Calendar</li><li>Contact Us</li></ul>
  </div>
  <div class="col-contact">
    <h3>Contact Detail</h3>
    <p>Lorem ipsum dolor sit 01<br>consectetur adipisic elit,<br>sed diam 1234</p>
    <p>01-5550-4821</p>
    <p>hello@miloscafe.com</p>
  </div>
  <div class="follow">
    <h3>Follow Us</h3>
    <ul><li><i></i>Friendspace</li><li><i></i>Chirpline</li><li><i></i>Workfolio</li></ul>
  </div>
</footer>
<div class="legal"><span>Copyright © 2013 Milo's Cafe. All Rights Reserved.</span><span>Privacy Policy | Terms &amp; Conditions</span></div>
</body>
</html>
```